Visitenkarte/Briefpapier für Coaching
Vielen Dank für die hervorragende Umsetzung meines Briefings und die super schnelle Bearbeitung meiner Kommentare. Das Ergebnis ist super! Gern empfehle ich Sie weiter.
Zielgruppe
Die Visitenkarte/Briefpapier soll sowohl Unternehmen als auch Privatpersonen aller Altersklassen ansprechen. Coaching hilft blockierende Verhaltensweisen zu überwinden, Ziele zu erreichen und alternative Wege im Handeln aufzuzeigen. Als Methode wird u.a. das flutstern-coaching eingesetzt (siehe www.flutstern.com). Anwendungsbeispiele sind: Flugangst, Prüfungsangst, Zahnbehandlungsangst, Beseitigung von Leistungs- und Kreativitätsblockaden, Burn-Out-Prophylaxe, Wettkampfvorbereitung, Teamcoaching usw.
Aufgabenstellung
Die Visitenkarte/Briefpapier soll Vertrauen, Zuverlässigkeit sowie die Merkmale des Coachings vermitteln. Mein Logo finden Sie als Datei angehängt. Dies sollte auf Seite 1 zu finden sein.
Ebenso meine Kontaktdaten:
Web: www.pfadlicht-coaching.de. Für Tel. Mobil, E-Mail und Internet hätte ich gern Symbole.
Auf Seite 2 der Visitenkarte möchte ich gern den Spruch: Wollen Sie Ihren Weg mit (hier flutstern-Logo aus Datei-Anhang einfügen, bitte Styleguide beachten)-Coaching finden?
Bei der Farbgestaltung der Visitenkarte/Briefpapier sollten sich die Farben aus dem Pfadlicht-Logo wiederfinden. Es darf auch gern ein farbiger Hintergrund sein.

```html
<!DOCTYPE html>
<html lang="de">
<head>
<meta charset="utf-8">
<title>flutstern – Visitenkarte Rückseite</title>
<link rel="stylesheet" href="https://fonts.googleapis.com/css2?family=Open+Sans:ital,wght@0,400;1,300&display=swap">
<style>
  :root {
    --paper: #ffffff;
    --ink: #1d1d1b;
    --ink-soft: #3a3a3a;
    --leaf-dark: #2f6b1f;
    --leaf-light: #7fb83a;
    --sun: #f4ae24;
    --photo-green-light: #7fae4e;
    --photo-green: #5a9434;
    --photo-green-deep: #3f7a25;
    --photo-pink: #eab2c6;
    --photo-rust: #a8553a;
  }
  html, body {
    margin: 0;
    padding: 0;
    width: 1200px;
    height: 777px;
    overflow: hidden;
    background: var(--paper);
  }
  .card {
    position: relative;
    width: 1200px;
    height: 777px;
    background: var(--paper);
    font-family: "Open Sans", Arial, sans-serif;
  }
  .card__art {
    position: absolute;
    inset: 0;
    display: block;
  }
  .card__tagline {
    position: absolute;
    left: 71px;
    top: 636px;
    margin: 0;
    font-style: italic;
    font-weight: 300;
    font-size: 35px;
    line-height: 38px;
    letter-spacing: 1px;
    color: var(--ink-soft);
  }
  .brand {
    position: absolute;
    left: 666px;
    top: 460px;
    width: 520px;
    height: 300px;
  }
  .brand__dot {
    position: absolute;
    left: 180px;
    top: 0;
    width: 164px;
    height: 164px;
    border-radius: 50%;
    background: var(--sun);
  }
  .brand__name {
    position: absolute;
    left: 0;
    top: 142px;
    margin: 0;
    font-family: "Open Sans", Arial, sans-serif;
    font-weight: 400;
    font-size: 112px;
    line-height: 120px;
    letter-spacing: -2px;
    color: var(--ink);
    white-space: nowrap;
  }
</style>
</head>
<body>
  <div class="card">
    <svg class="card__art" viewBox="0 0 1200 777" width="1200" height="777">
      <defs>
        <linearGradient id="meadow" x1="0" y1="0" x2="1" y2="1">
          <stop offset="0" stop-color="var(--photo-green-light)"/>
          <stop offset="0.5" stop-color="var(--photo-green)"/>
          <stop offset="1" stop-color="var(--photo-green-deep)"/>
        </linearGradient>
        <filter id="soften" x="-50%" y="-50%" width="200%" height="200%">
          <feGaussianBlur stdDeviation="55"/>
        </filter>
        <linearGradient id="swoosh" x1="0" y1="0" x2="1" y2="0">
          <stop offset="0" stop-color="var(--leaf-dark)"/>
          <stop offset="0.5" stop-color="var(--leaf-light)"/>
          <stop offset="1" stop-color="var(--leaf-dark)"/>
        </linearGradient>
        <clipPath id="photoArea">
          <rect x="0" y="0" width="1200" height="600"/>
        </clipPath>
      </defs>

      <g class="photo" clip-path="url(#photoArea)" role="img"
         aria-label="Foto: Tagpfauenauge mit geöffneten Flügeln auf rosa Fetthennen-Blüten vor grünem Hintergrund">
        <rect x="0" y="0" width="1200" height="600" fill="url(#meadow)"/>
        <g filter="url(#soften)">
          <ellipse cx="110" cy="90" rx="150" ry="110" fill="var(--photo-pink)" opacity="0.75"/>
          <ellipse cx="600" cy="30" rx="260" ry="90" fill="var(--photo-pink)" opacity="0.7"/>
          <ellipse cx="440" cy="470" rx="200" ry="90" fill="var(--photo-pink)" opacity="0.8"/>
          <ellipse cx="520" cy="250" rx="230" ry="120" fill="var(--photo-rust)" opacity="0.55"/>
        </g>
      </g>

      <path class="paper" fill="var(--paper)"
            d="M0,488 C220,476 430,512 538,592 C700,470 950,338 1200,302 L1200,777 L0,777 Z"/>

      <path class="swoosh swoosh--left" fill="none" stroke="url(#swoosh)" stroke-width="6"
            d="M0,478 C220,466 430,502 536,582"/>
      <path class="swoosh swoosh--right" fill="none" stroke="url(#swoosh)" stroke-width="6"
            d="M542,582 C700,462 950,326 1200,292"/>
      <path class="swoosh-line" fill="none" stroke="var(--paper)" stroke-width="2"
            d="M0,470 C220,458 430,494 536,574 M542,574 C700,454 950,318 1200,284"/>
    </svg>

    <p class="card__tagline">Sie wollen Ihren Weg mit<br>flutstern-Coaching finden?</p>

    <div class="brand">
      <span class="brand__dot"></span>
      <p class="brand__name">flutstern</p>
    </div>
  </div>
</body>
</html>
```